Marlowe Holdings LLC - Business Cards

Need the following information on the cards:

Name: Dean R Vossler
Title: Chief Executive Manager

Business address:
412 N Ridgeview Lane #118
Carol Stream, Il 60412

Phone: (630) 555-0148 - Business
KPV FFL license number: 5-21-xxx-xx-xx-04519
Email: dean.vossler@marloweholdingsffl.com

Target Market(s)

Firearm owners

Industry/Entity Type

Firearms industry,

Contact Information for Business Card

Contact number, name and title, web page address, email, business address and kpv license number,

Requirements
Must have
• Name, title, business address, phone numbers, KPV license numbers, web page address and email address.
Nice to have
• Cellphone number,

```html
<!DOCTYPE html>
<html lang="en">
<head>
<meta charset="utf-8">
<title>Marlowe Holdings LLC – Business Cards</title>
<link rel="stylesheet" href="https://fonts.googleapis.com/css2?family=Lato:wght@400;700&family=Montserrat:wght@700&display=swap">
<style>
  :root {
    --backdrop: #858585;
    --card-dark: #231f20;
    --brand-red: #c91a22;
    --paper: #eeeced;
    --ink: #231f20;
    --white: #ffffff;
  }
  * { margin: 0; padding: 0; box-sizing: border-box; }
  html, body { width: 1075px; height: 1200px; overflow: hidden; }
  body {
    background: var(--backdrop);
    font-family: "Lato", sans-serif;
    position: relative;
  }
  .card {
    position: absolute;
    width: 664px;
    height: 396px;
    box-shadow: 3px 3px 2px rgba(0,0,0,0.55);
    overflow: hidden;
  }
  .card-front { left: 206px; top: 187px; background: var(--card-dark); color: var(--white); }
  .card-back { left: 203px; top: 638px; background: var(--paper); }

  .art-panel {
    position: absolute; left: 440px; top: 0; width: 224px; height: 396px;
    background: var(--brand-red);
  }

  .holder-name {
    position: absolute; left: 25px; top: 62px;
    font-family: "Montserrat", sans-serif; font-weight: 700;
    font-size: 22px; letter-spacing: 0.3px; color: var(--brand-red);
    text-transform: uppercase; line-height: 1;
  }
  .holder-title {
    position: absolute; left: 25px; top: 87px;
    font-size: 17px; line-height: 1;
  }
  .address {
    position: absolute; left: 26px; top: 169px;
    font-size: 17px; line-height: 23px; font-style: normal;
  }
  .contact-list {
    position: absolute; left: 26px; top: 273px;
    list-style: none; font-size: 17px;
  }
  .contact-list li { display: flex; align-items: center; height: 23.5px; }
  .contact-list svg { width: 15px; height: 15px; margin-right: 6px; fill: var(--brand-red); flex: none; }

  .company-mark {
    position: absolute; left: 0; right: 0; top: 160px;
    display: flex; align-items: center; justify-content: center; gap: 12px;
  }
  .company-dot { width: 16px; height: 16px; border-radius: 50%; background: var(--brand-red); }
  .company-name {
    font-weight: 700; font-size: 30px; color: var(--brand-red);
  }
  .license {
    position: absolute; left: 56px; right: 60px; top: 344px;
    display: flex; align-items: center; gap: 10px;
    font-size: 17.5px; color: var(--ink); white-space: nowrap;
  }
  .license::before, .license::after { content: ""; flex: 1; height: 1px; background: var(--ink); }
  .license-label { color: var(--brand-red); }
</style>
</head>
<body>

<section class="card card-front">
  <div class="art-panel" role="img" aria-label="Large red illustration of a standing dog outlined in white"></div>

  <h1 class="holder-name">Dean R Vossler</h1>
  <p class="holder-title">Chief Executive Manager</p>

  <address class="address">412 N Ridgeview Lane #118<br>Carol Stream, Il 60412</address>

  <ul class="contact-list">
    <li><svg viewBox="0 0 24 24"><path d="M6.6 10.8a15 15 0 0 0 6.6 6.6l2.2-2.2a1 1 0 0 1 1-.25 11.4 11.4 0 0 0 3.6.57 1 1 0 0 1 1 1V20a1 1 0 0 1-1 1A17 17 0 0 1 3 4a1 1 0 0 1 1-1h3.5a1 1 0 0 1 1 1c0 1.25.2 2.45.57 3.57a1 1 0 0 1-.25 1z"/></svg>(630) 555-0148</li>
    <li><svg viewBox="0 0 24 24"><path d="M7 1h10a2 2 0 0 1 2 2v18a2 2 0 0 1-2 2H7a2 2 0 0 1-2-2V3a2 2 0 0 1 2-2zm0 3v14h10V4zm5 15.5a1.2 1.2 0 1 0 0 2.4 1.2 1.2 0 0 0 0-2.4z"/></svg>(630) 555-0148</li>
    <li><svg viewBox="0 0 24 24"><path d="M2 5h20v14H2zm2 2v.4l8 5.2 8-5.2V7z"/></svg>dean.vossler@marloweholdingsffl.com</li>
    <li><svg viewBox="0 0 24 24"><path d="M12 2a10 10 0 1 0 0 20 10 10 0 0 0 0-20zm6.9 6h-2.9a15 15 0 0 0-1.4-3.6A8 8 0 0 1 18.9 8zM12 4c.8 1.2 1.5 2.5 1.9 4h-3.8c.4-1.5 1.1-2.8 1.900-4zM4.3 14a8 8 0 0 1 0-4h3.4a16 16 0 0 0 0 4zm.8 2h2.9c.3 1.3.8 2.5 1.4 3.6A8 8 0 0 1 5.1 16zM8 8H5.1a8 8 0 0 1 4.3-3.6C8.8 5.5 8.3 6.7 8 8zm4 12c-.8-1.2-1.5-2.5-1.9-4h3.8c-.4 1.5-1.1 2.8-1.9 4zm2.3-6H9.7a14 14 0 0 1 0-4h4.6a14 14 0 0 1 0 4zm.3 5.6c.6-1.1 1.1-2.3 1.4-3.6h2.9a8 8 0 0 1-4.3 3.6zm1.7-5.6a16 16 0 0 0 0-4h3.4a8 8 0 0 1 0 4z"/></svg>www.marloweholdingsffl.com</li>
  </ul>
</section>

<section class="card card-back">
  <div class="company-mark">
    <span class="company-dot"></span>
    <span class="company-name">Marlowe Holdings LLC</span>
  </div>
  <p class="license"><span><span class="license-label">KPV FFL License No:</span> 5-21-xxx-xx-xx-04519</span></p>
</section>

</body>
</html>
```